Night Dresses business cards business requirers

We are a new company initiating Mexico operations. Our core business is Night woman dress (both formal and party dress) for rent. Gownhaven is the name of the company. ITS Gownhaven form by two word. The dress word and topia (Utopic) so the place Gownhaven Means That You cant get the ideal, perfect and unique dress for your event. So we would like a modern, very creative, and attractive business card.

Industry/Entity Type

Womens Clothing

Contact Information for Business Card

Rounded Borders, two faces

Requirements
Must have
• Rounded borders, logo and slogan, modern, glam, attractive design
Should not have
• modern design classic or not

```html
<!DOCTYPE html>
<html lang="en">
<head>
<meta charset="utf-8">
<title>Gownhaven Business Cards</title>
<link rel="stylesheet" href="https://fonts.googleapis.com/css2?family=Montserrat:wght@400;500&family=Roboto:wght@300;400&display=swap">
<style>
  :root {
    --backdrop: #8c8c8a;
    --paper: #ffffff;
    --plum: #9c3a7c;
    --plum-deep: #7d2a62;
    --ink-grey: #9a9a9a;
    --ink-dark: #333333;
    --wine: #8a1232;
    --wine-dark: #1c0308;
    --white: #ffffff;
  }
  * { box-sizing: border-box; margin: 0; padding: 0; }
  html, body { width: 1200px; height: 960px; overflow: hidden; }
  body {
    background: var(--backdrop);
    position: relative;
    font-family: "Roboto", Arial, sans-serif;
  }
  .card {
    position: absolute;
    left: 290px;
    width: 620px;
    height: 354px;
    border-radius: 18px;
    overflow: hidden;
  }
  .card-front { top: 70px; background: var(--paper); }
  .card-back { top: 536px; }

  .side-panel { position: absolute; inset: 0; width: 100%; height: 100%; }

  .brand {
    position: absolute;
    display: flex;
    align-items: center;
    gap: 12px;
  }
  .brand-dot {
    width: 40px; height: 40px;
    border-radius: 50%;
    border: 3px solid var(--plum);
    flex: none;
  }
  .brand-text { display: flex; flex-direction: column; align-items: center; }
  .brand-name {
    font-family: "Montserrat", Arial, sans-serif;
    font-weight: 500;
    letter-spacing: 0.28em;
    color: var(--ink-dark);
    font-size: 19px;
    line-height: 1.1;
  }
  .brand-slogan {
    font-family: "Montserrat", Arial, sans-serif;
    font-weight: 500;
    font-size: 9px;
    letter-spacing: 0.3em;
    color: var(--ink-dark);
    margin-top: 4px;
  }
  .card-front .brand { left: 40px; top: 44px; }

  .holder-name {
    position: absolute;
    left: 44px; top: 166px;
    font-weight: 300;
    font-size: 25px;
    color: var(--ink-grey);
  }
  .contact-list {
    position: absolute;
    left: 40px; top: 225px;
    list-style: none;
    font-size: 15px;
    font-weight: 300;
    color: var(--ink-grey);
  }
  .contact-list li { display: flex; align-items: center; gap: 8px; height: 21px; }
  .contact-icon { width: 14px; height: 14px; flex: none; }
  .social-dot {
    width: 12px; height: 12px; margin: 0 1px;
    border-radius: 50%; background: var(--plum); flex: none;
  }

  .pattern-field {
    position: absolute; inset: 0;
    background: radial-gradient(ellipse at 50% 45%, var(--wine) 0%, #5a0a20 45%, var(--wine-dark) 100%);
  }
  .card-back .brand {
    left: 50%; top: 50%;
    transform: translate(-50%, -50%);
    flex-direction: column;
    gap: 14px;
  }
  .card-back .brand-dot {
    width: 72px; height: 72px;
    border: 4px solid var(--white);
  }
  .card-back .brand-name { color: var(--white); font-size: 24px; }
  .card-back .brand-slogan { color: var(--white); font-size: 11px; }
</style>
</head>
<body>
  <section class="card card-front" aria-label="Card front">
    <svg class="side-panel" viewBox="0 0 620 354" preserveAspectRatio="none" aria-hidden="true">
      <polygon points="340,0 620,0 620,354 520,354" fill="var(--plum)"/>
      <polygon points="340,0 356,0 534,354 520,354" fill="var(--plum-deep)"/>
      <circle cx="520" cy="110" r="82" fill="none" stroke="var(--plum-deep)" stroke-width="5" opacity="0.55"/>
    </svg>

    <div class="brand">
      <span class="brand-dot"></span>
      <div class="brand-text">
        <span class="brand-name">GOWNHAVEN</span>
        <span class="brand-slogan">NIGHTS IN STYLE</span>
      </div>
    </div>

    <p class="holder-name">Marco Villeneuve R.</p>

    <ul class="contact-list">
      <li>
        <svg class="contact-icon" viewBox="0 0 24 24" aria-hidden="true">
          <path d="M6.6 10.8a15.1 15.1 0 0 0 6.6 6.6l2.2-2.2a1 1 0 0 1 1-.25 11.4 11.4 0 0 0 3.6.57 1 1 0 0 1 1 1V20a1 1 0 0 1-1 1A17 17 0 0 1 3 4a1 1 0 0 1 1-1h3.5a1 1 0 0 1 1 1c0 1.25.2 2.45.57 3.6a1 1 0 0 1-.25 1z" fill="var(--plum)"/>
        </svg>
        555-210-7384
      </li>
      <li>
        <svg class="contact-icon" viewBox="0 0 24 24" aria-hidden="true">
          <rect x="2" y="5" width="20" height="14" rx="2" fill="none" stroke="var(--plum)" stroke-width="2"/>
          <path d="M3 6l9 7 9-7" fill="none" stroke="var(--plum)" stroke-width="2"/>
        </svg>
        marcovilleneuve@gownhaven.com
      </li>
      <li>
        <span class="social-dot"></span>
        @gownhaven
      </li>
    </ul>
  </section>

  <section class="card card-back" aria-label="Card back">
    <div class="pattern-field" role="img" aria-label="Dark red and black damask pattern background"></div>
    <div class="brand">
      <span class="brand-dot"></span>
      <div class="brand-text">
        <span class="brand-name">GOWNHAVEN</span>
        <span class="brand-slogan">NIGHTS IN STYLE</span>
      </div>
    </div>
  </section>
</body>
</html>
```